Business Card Design

Please copy the format of the attached card.

FRONT:
White text small blue horses head logo where "mirano" in in example

BACK:
Blue background w/ white horses head

Industry/Entity Type

Business

Contact Information for Business Card

Dalton Greer
Chief Executive Officer
Tarnwick Inns & Resorts
417 Fenmore Street | San Francisco, California 94632
Tel: +1.310.555.0184
email: dalton@tarnwickinns-example.com

```html
<!DOCTYPE html>
<html lang="en">
<head>
<meta charset="utf-8">
<title>Tarnwick Inns &amp; Resorts — Business Card</title>
<link rel="stylesheet" href="https://fonts.googleapis.com/css2?family=Arimo:wght@400&display=swap">
<style>
  :root {
    --backdrop: #2a2a2a;
    --navy: #1f447e;
    --white: #ffffff;
    --card-shadow: rgba(0, 0, 0, 0.45);
  }
  * { box-sizing: border-box; margin: 0; padding: 0; }
  html, body {
    width: 1200px;
    height: 900px;
    overflow: hidden;
    background: var(--backdrop);
    font-family: "Arimo", Arial, sans-serif;
  }
  .canvas {
    position: relative;
    width: 1200px;
    height: 900px;
  }
  .card {
    position: absolute;
    width: 560px;
    height: 320px;
    box-shadow: 0 14px 30px var(--card-shadow);
  }
  .card--contact {
    left: 150px;
    top: 120px;
    background: var(--navy);
    color: var(--white);
  }
  .card--brand {
    left: 490px;
    top: 460px;
    background: var(--white);
    color: var(--navy);
    display: flex;
    flex-direction: column;
    align-items: center;
    justify-content: center;
  }

  /* contact side */
  .brand-mark {
    position: absolute;
    left: 52px;
    top: 62px;
    display: flex;
    align-items: center;
    gap: 10px;
    font-size: 17px;
    letter-spacing: 0.02em;
  }
  .brand-mark__dot {
    width: 14px;
    height: 14px;
    border-radius: 50%;
    background: currentColor;
  }
  .contact {
    position: absolute;
    left: 52px;
    top: 150px;
    line-height: 1.2;
  }
  .contact__name {
    font-size: 22px;
    margin-bottom: 14px;
  }
  .contact__title {
    font-size: 13px;
  }
  .contact__company,
  .contact__address,
  .contact__line {
    font-size: 13.5px;
  }
  .contact__lines {
    margin-top: 18px;
  }

  /* brand side */
  .brand-lockup {
    display: flex;
    align-items: center;
    gap: 14px;
    font-size: 30px;
    margin-top: 30px;
  }
  .brand-lockup__dot {
    width: 18px;
    height: 18px;
    border-radius: 50%;
    background: currentColor;
  }
  .website {
    margin-top: 40px;
    font-size: 14px;
    letter-spacing: 0.32em;
  }
</style>
</head>
<body>
<main class="canvas">
  <section class="card card--contact" aria-label="Business card, contact side">
    <div class="brand-mark">
      <span class="brand-mark__dot" aria-hidden="true"></span>
      <span class="brand-mark__name">Tarnwick</span>
    </div>
    <div class="contact">
      <p class="contact__name">Dalton Greer <span class="contact__title">| Chief Executive Officer</span></p>
      <p class="contact__company">Tarnwick Inns &amp; Resorts</p>
      <p class="contact__address">417 Fenmore Street | San Francisco, California 94632</p>
      <div class="contact__lines">
        <p class="contact__line">tel: +1.310.555.0184</p>
        <p class="contact__line">email: dalton@tarnwickinns-example.com</p>
      </div>
    </div>
  </section>

  <section class="card card--brand" aria-label="Business card, brand side">
    <div class="brand-lockup">
      <span class="brand-lockup__dot" aria-hidden="true"></span>
      <span class="brand-lockup__name">Tarnwick Inns &amp; Resorts</span>
    </div>
    <p class="website">www.tarnwickinns-example.com</p>
  </section>
</main>
</body>
</html>
```